Christmas Candle Label

We require a Christmas candle label that fits with our current brand (see larkfieldcandleworks.com.au, and also example attached). On the attached we would like the word 'Marlowe - Pendleby' replaced with 'Merry Christmas' (or something creative that you can come up with) and the writing on the left hand side 'lose yourself in the subtle.........' replaced with 'its beginning to smell a lot like Christmas' (or something creative that you can come up with). We would like the flora image in the background replaced with a line drawing of a Christmas tree or holy or anything else that is appropriate. Finally we are not sure if a different colour label i.e. red, maroon or green (with lots of black, silver or gold writing) instead of black would be best for this label. It may be best to see a comparison of our original black label with black, silver or gold writing, and the other colours.

```html
<!DOCTYPE html>
<html lang="en">
<head>
<meta charset="utf-8">
<title>Christmas Candle Label</title>
<link href="https://fonts.googleapis.com/css2?family=Cinzel:wght@400&family=Alegreya:wght@400&family=Poppins:wght@400&display=swap" rel="stylesheet">
<style>
  :root {
    --page-bg: #d9d9d9;
    --label-red: #c4140b;
    --label-red-mid: #a80c08;
    --label-red-deep: #8c0606;
    --gold: #e6c77a;
    --gold-soft: rgba(230, 199, 122, 0.16);
    --gold-faint: rgba(230, 199, 122, 0.05);
    --white: #ffffff;
    --white-soft: rgba(255, 255, 255, 0.12);
    --white-faint: rgba(255, 255, 255, 0.03);
  }
  html, body {
    margin: 0;
    padding: 0;
    width: 1152px;
    height: 1200px;
    overflow: hidden;
    background: var(--page-bg);
  }
  .label {
    position: absolute;
    left: 40px;
    top: 377px;
    width: 1072px;
    height: 446px;
    overflow: hidden;
    background: radial-gradient(ellipse 60% 75% at 45% 45%, var(--label-red) 0%, var(--label-red-mid) 55%, var(--label-red-deep) 100%);
  }
  .art {
    position: absolute;
    border-radius: 6px;
  }
  .art--baubles {
    left: 40px; top: 0; width: 192px; height: 166px;
    background: linear-gradient(180deg, var(--gold-faint) 0%, var(--gold-soft) 100%);
  }
  .art--tree {
    left: 608px; top: 14px; width: 272px; height: 432px;
    border-radius: 6px 6px 0 0;
    background: linear-gradient(180deg, rgba(255, 170, 70, 0.20) 0%, var(--gold-faint) 30%, var(--gold-soft) 85%, var(--gold-faint) 100%);
  }
  .art--flakes {
    left: 920px; top: 100px; width: 152px; height: 138px;
    border-radius: 6px 0 0 6px;
    background: linear-gradient(90deg, var(--white-soft) 0%, var(--gold-soft) 100%);
  }
  .brand-name {
    position: absolute;
    left: 322px; top: 32px;
    margin: 0;
    font-family: "Poppins", sans-serif;
    font-weight: 400;
    font-size: 15.5px;
    line-height: 17.5px;
    color: var(--white);
  }
  .greeting {
    position: absolute;
    left: 31px; top: 174px;
    margin: 0;
    font-family: "Alegreya", serif;
    font-size: 23px;
    line-height: 30.4px;
    color: var(--gold);
  }
  .headline {
    position: absolute;
    left: 318px; top: 168px;
    width: 300px;
    margin: 0;
    text-align: center;
    font-family: "Cinzel", serif;
    font-weight: 400;
    font-size: 52px;
    line-height: 52px;
    letter-spacing: -0.5px;
    color: var(--gold);
  }
  .origin {
    position: absolute;
    left: 322px; top: 380px;
    margin: 0;
    font-family: "Alegreya", serif;
    font-size: 19px;
    line-height: 19px;
    letter-spacing: 0.5px;
    color: var(--gold);
  }
  .batch {
    position: absolute;
    left: 890px; top: 31px;
    width: 160px;
    height: 20px;
    margin: 0;
    font-family: "Alegreya", serif;
    font-size: 15px;
    line-height: 20px;
    color: var(--gold);
  }
  .batch__slash {
    position: absolute;
    top: 0;
  }
  .batch__slash--day { left: 104px; }
  .batch__slash--month { left: 145px; }
  .details {
    position: absolute;
    right: 30px; top: 284px;
    margin: 0;
    text-align: right;
    font-family: "Poppins", sans-serif;
    font-size: 13.5px;
    line-height: 17px;
    color: var(--white);
  }
  .details p { margin: 0 0 6px; }
</style>
</head>
<body>
  <section class="label">
    <div class="art art--baubles" role="img" aria-label="Gold line-drawn Christmas baubles hanging on strings with small snowflakes"></div>
    <div class="art art--tree" role="img" aria-label="Gold swirling line-drawn Christmas tree topped with a glowing star"></div>
    <div class="art art--flakes" role="img" aria-label="White and gold snowflakes"></div>

    <p class="brand-name">Quiet Ridge<br>Woodland</p>

    <p class="greeting">Warmest<br>greetings<br>of this<br>festive<br>season and<br>best wishes<br>for happiness<br>in the New Year..</p>

    <h1 class="headline">Merry<br>Christmas</h1>

    <p class="origin">Handcrafted in<br>Southern Tasmania</p>

    <p class="batch">Batch No.<span class="batch__slash batch__slash--day">/</span><span class="batch__slash batch__slash--month">/</span></p>

    <div class="details">
      <p>500g<br>90+ hours</p>
      <p>Hand poured,<br>scented soy and<br>coconut candle</p>
      <p>Made with all<br>natural ingredients</p>
    </div>
  </section>
</body>
</html>
```